Business Card Design

We are state certified residental contractors who specialize in insurance claims. We are insurance restoration experts and have a state multi-lines insurance adjusters license #W584130. We produce insurance grade estimates using the most widely used software in the industry. Our goal is to work for our customers! not the insurance company. Our edge is we don't take short cuts to please the adjuster/insurance company to insure future claims from them. We are experts at restoring damaged properties.from wind, water ,fire and smoke. We pride ourselfs on evaluating damages properly and providing extremely detailed estimates for restoration.We are also educated and experienced in identifiying and correcting indoor air quality issues as a result of common perils and defective materials. .We are not a franchise and are family owned and operated. We provide quality work using only the best local tradesman. We ourselfs are local tradesmen and helped build and restore our community over the past 30 years. We know first hand how our homes were built and are aware of many of the common problems that exist and how to address them. We are licensed insured and bonded.
Industry/Entity Type
Business
Contact Information for Business Card
Beacon Harbor LLC
Marcus Pelley
4185 Willowbend Rd unit K
Melbourne Fl.32937 Manager/State Certified Residental Contractor license# CRC5871642
321-555-0187 Office
321-555-0162 Fax

```html
<!DOCTYPE html>
<html lang="en">
<head>
<meta charset="utf-8">
<title>Beacon Harbor LLC – Business Card</title>
<link rel="stylesheet" href="https://fonts.googleapis.com/css2?family=Exo+2:wght@700;800&family=Roboto:wght@400;500&display=swap">
<style>
  :root {
    --backdrop: #e9e6e1;
    --card: #ffffff;
    --gold: #a59a2c;
    --ink: #262426;
    --charcoal: #2c2a2c;
    --shadow: rgba(0,0,0,0.18);
  }
  * { margin: 0; padding: 0; box-sizing: border-box; }
  html, body { width: 1200px; height: 892px; overflow: hidden; }
  body {
    background: var(--backdrop);
    font-family: "Roboto", Arial, sans-serif;
    color: var(--ink);
    position: relative;
  }
  .card {
    position: absolute;
    top: 291px;
    width: 540px;
    height: 309px;
    background: var(--card);
    box-shadow: 0 8px 24px var(--shadow);
    overflow: hidden;
  }
  .card--front { left: 40px; }
  .card--back { left: 620px; }
  .card__wave { position: absolute; left: 0; top: 0; width: 540px; height: 309px; }

  .brand {
    position: absolute;
    display: flex;
    align-items: center;
    gap: 12px;
    font-family: "Exo 2", Arial, sans-serif;
    font-weight: 800;
    color: var(--gold);
    text-transform: uppercase;
    letter-spacing: 0.5px;
    line-height: 1;
    z-index: 1;
  }
  .brand__dot { width: 30px; height: 30px; border-radius: 50%; background: var(--gold); flex: none; }

  .card--front .brand { left: 26px; top: 26px; font-size: 34px; }
  .card--back .brand {
    left: 0; right: 0; top: 50px;
    flex-direction: column; gap: 16px;
    font-size: 38px;
  }
  .card--back .brand__dot { width: 44px; height: 44px; }

  .contact { position: absolute; left: 30px; top: 76px; z-index: 1; }
  .contact__name {
    font-family: "Exo 2", Arial, sans-serif;
    font-weight: 800;
    font-size: 22px;
    text-transform: uppercase;
    line-height: 1;
  }
  .contact__title, .contact__license { font-size: 10px; line-height: 1.3; }
  .contact__title { margin-top: 4px; }
  .contact__address { font-size: 14px; margin-top: 8px; line-height: 1.2; }
  .contact__line { display: flex; align-items: center; gap: 8px; font-size: 14px; margin-top: 4px; line-height: 1.2; }
  .contact__icon {
    width: 16px; height: 16px; background: var(--gold); border-radius: 3px;
    display: flex; align-items: center; justify-content: center;
  }
</style>
</head>
<body>

<section class="card card--front" aria-label="Business card front">
  <svg class="card__wave" viewBox="0 0 540 309" aria-hidden="true">
    <path d="M0 212 C120 220 260 256 360 266 C440 274 500 286 540 300 L540 309 L0 309 Z" fill="var(--gold)"/>
    <path d="M0 225 C120 235 250 267 350 277 C430 285 495 293 540 306 L540 309 L0 309 Z" fill="var(--card)"/>
    <path d="M0 231 C120 242 250 274 350 284 C430 292 495 300 540 309 L0 309 Z" fill="var(--charcoal)"/>
  </svg>

  <div class="brand"><span class="brand__dot"></span><span>Beacon Harbor LLC</span></div>

  <div class="contact">
    <p class="contact__name">Marcus Pelley</p>
    <p class="contact__title">Manager/State Certified Residental Contractor</p>
    <p class="contact__license">license# CRC5871642</p>
    <p class="contact__address">4185 Willowbend Rd unit K Melbourne Fl.32937</p>
    <p class="contact__line">
      <span class="contact__icon" aria-label="Office">
        <svg width="10" height="10" viewBox="0 0 24 24"><path fill="#fff" d="M6.6 10.8a15 15 0 0 0 6.6 6.6l2.2-2.2a1 1 0 0 1 1-.25 11.4 11.4 0 0 0 3.6.57 1 1 0 0 1 1 1V20a1 1 0 0 1-1 1A17 17 0 0 1 3 4a1 1 0 0 1 1-1h3.5a1 1 0 0 1 1 1c0 1.25.2 2.45.57 3.57a1 1 0 0 1-.25 1z"/></svg>
      </span>321-555-0187
    </p>
    <p class="contact__line">
      <span class="contact__icon" aria-label="Fax">
        <svg width="10" height="10" viewBox="0 0 24 24"><path fill="#fff" d="M6 2h12v5H6zM3 8h18a1 1 0 0 1 1 1v8h-4v5H6v-5H2V9a1 1 0 0 1 1-1zm5 8v4h8v-4z"/></svg>
      </span>321-555-0162
    </p>
  </div>
</section>

<section class="card card--back" aria-label="Business card back">
  <svg class="card__wave" viewBox="0 0 540 309" aria-hidden="true">
    <path d="M0 196 C110 212 250 248 360 260 C440 268 500 282 540 298 L540 309 L0 309 Z" fill="var(--gold)"/>
    <path d="M0 210 C110 228 250 262 350 272 C430 280 495 292 540 306 L540 309 L0 309 Z" fill="var(--card)"/>
    <path d="M0 216 C110 235 250 269 350 279 C430 287 495 299 540 309 L0 309 Z" fill="var(--charcoal)"/>
  </svg>

  <div class="brand"><span class="brand__dot"></span><span>Beacon Harbor LLC</span></div>
</section>

</body>
</html>
```